business cards, stationary
lets see what you got
Use specific fonts
up to designer
Modern
Calvin Marsh
Director of Sales
1870 Quarrymill road, Suite 114 Burlington, On L4K 3P8
Calvin@sunlanejourneys.example
www.sunlanejourneys.example
BBM: 58720936
LOGO on back

```html
<!DOCTYPE html>
<html lang="en">
<head>
<meta charset="utf-8">
<title>Calvin Marsh – Business Card</title>
<link href="https://fonts.googleapis.com/css2?family=Open+Sans:wght@400;600;700&display=swap" rel="stylesheet">
<style>
  :root {
    --backdrop: #2f2f31;
    --card: #ffffff;
    --purple: #5c2e84;
    --green: #8dc63f;
    --text-light: #ffffff;
    --text-muted: #e6dcef;
  }
  html, body {
    margin: 0;
    width: 1200px;
    height: 780px;
    overflow: hidden;
    background: var(--backdrop);
    font-family: "Open Sans", Arial, sans-serif;
  }
  .card {
    position: absolute;
    left: 75px;
    top: 90px;
    width: 1050px;
    height: 600px;
    border-radius: 36px;
    background: var(--card);
    overflow: hidden;
  }
  .card-bands {
    position: absolute;
    inset: 0;
    width: 100%;
    height: 100%;
  }
  .brand {
    position: absolute;
    top: 118px;
    left: 160px;
    display: flex;
    align-items: center;
    gap: 22px;
    white-space: nowrap;
  }
  .brand-dot {
    width: 58px;
    height: 58px;
    border-radius: 50%;
    background: var(--green);
    flex: none;
  }
  .brand-name {
    font-size: 46px;
    font-weight: 700;
    color: var(--purple);
    letter-spacing: -1px;
  }
  .identity {
    position: absolute;
    right: 590px;
    top: 372px;
    text-align: right;
    color: var(--text-light);
    white-space: nowrap;
  }
  .identity-name {
    margin: 0;
    font-size: 34px;
    font-weight: 700;
    line-height: 1.1;
  }
  .identity-title {
    margin: 2px 0 0;
    font-size: 22px;
    font-weight: 600;
    color: var(--text-muted);
  }
  .identity-address {
    margin: 34px 0 0;
    font-size: 21px;
    line-height: 1.4;
    font-style: normal;
  }
  .divider {
    position: absolute;
    left: 498px;
    top: 378px;
    width: 2px;
    height: 168px;
    background: var(--text-light);
    opacity: 0.85;
  }
  .contacts {
    position: absolute;
    left: 522px;
    top: 372px;
    margin: 0;
    padding: 0;
    list-style: none;
    color: var(--text-light);
    font-size: 21px;
    white-space: nowrap;
  }
  .contacts li {
    display: flex;
    align-items: center;
    gap: 18px;
    height: 44px;
  }
  .contact-icon {
    width: 22px;
    height: 22px;
    flex: none;
  }
</style>
</head>
<body>
  <main class="card">
    <svg class="card-bands" viewBox="0 0 1050 600" aria-hidden="true">
      <path d="M0 290 C260 250 520 235 760 232 C480 262 230 320 0 400 Z" fill="var(--green)"/>
      <path d="M0 400 C230 320 480 262 760 232 C860 228 960 226 1050 228 L1050 600 L0 600 Z" fill="var(--purple)"/>
    </svg>

    <div class="brand">
      <span class="brand-dot"></span>
      <span class="brand-name">sunlanejourneys.example</span>
    </div>

    <section class="identity">
      <h1 class="identity-name">Calvin Marsh</h1>
      <p class="identity-title">Director of Sales</p>
      <address class="identity-address">1870 Quarrymill road,<br>Suite 114, Burlington, On L4K 3P8</address>
    </section>

    <div class="divider"></div>

    <ul class="contacts">
      <li>
        <svg class="contact-icon" viewBox="0 0 24 24"><path d="M6.6 10.8a15 15 0 0 0 6.6 6.6l2.2-2.2a1 1 0 0 1 1-.25 11.4 11.4 0 0 0 3.6.57 1 1 0 0 1 1 1V20a1 1 0 0 1-1 1A17 17 0 0 1 3 4a1 1 0 0 1 1-1h3.5a1 1 0 0 1 1 1c0 1.25.2 2.45.57 3.57a1 1 0 0 1-.25 1z" fill="#fff"/></svg>
        <span>1.800.555.0142</span>
      </li>
      <li>
        <svg class="contact-icon" viewBox="0 0 24 24"><rect x="6" y="2" width="12" height="20" rx="2" fill="none" stroke="#fff" stroke-width="2"/><circle cx="12" cy="18" r="1.3" fill="#fff"/></svg>
        <span>705.555.0188</span>
      </li>
      <li>
        <svg class="contact-icon" viewBox="0 0 24 24"><text x="12" y="18" text-anchor="middle" font-family="Open Sans, Arial, sans-serif" font-size="20" font-weight="700" fill="#fff">@</text></svg>
        <span>Calvin@sunlanejourneys.example</span>
      </li>
      <li>
        <svg class="contact-icon" viewBox="0 0 24 24" fill="none" stroke="#fff" stroke-width="1.8"><circle cx="12" cy="12" r="9.5"/><ellipse cx="12" cy="12" rx="4" ry="9.5"/><path d="M2.5 12h19M4 7h16M4 17h16"/></svg>
        <span>www.sunlanejourneys.example</span>
      </li>
    </ul>
  </main>
</body>
</html>
```